Business Document/Catalogue Cover Page

Update: Please include image of grease products as provided, the blue bearing and the letter K with Swirl outline (or as simialr element). We want to create a sleek, professional and simplistic design A4 cover page for all of our documents to keep branding consistent.
We are an industrial lubricant company based in Australia. please refer to similar companies for inspiration if you wish.
Use blues and greys and elements to tie in logo and images to include. (some blue or grey colour gradients or reduced transparency elements look good also).
Include a heading e.g PRODUCT RANGE in Roboto font.
Feel free to introduce your own elements that will elevate the design.

Industry/Entity Type

Lubricants/Industrial

Font styles to use
Other font styles liked:
• Roboto

Colors
0054AA
0677BA
7BADD7
CADEEF
E8F1F8

Requirements
Must have
• VOREN LOGO

```html
<!DOCTYPE html>
<html lang="en">
<head>
<meta charset="UTF-8">
<title>VOREN Australia – Product Range</title>
<link href="https://fonts.googleapis.com/css2?family=Roboto:wght@100;300;400;700&display=swap" rel="stylesheet">
<style>
  :root {
    --page-bg: #ececec;
    --navy: #1b2a6e;
    --brand-blue: #0054aa;
    --mid-blue: #0677ba;
    --light-blue: #7badd7;
    --pale-blue: #cadeef;
    --ice-blue: #e8f1f8;
    --steel: #c9ccd4;
    --steel-dark: #6d7384;
    --ribbon-deep: #1d2f93;
    --ribbon-bright: #3a52c9;
    --label-bg: #eeeff1;
    --white: #ffffff;
  }
  * { box-sizing: border-box; margin: 0; padding: 0; }
  html, body {
    width: 1200px;
    height: 900px;
    overflow: hidden;
    background: var(--page-bg);
    font-family: "Roboto", Arial, sans-serif;
  }
  .cover {
    position: absolute;
    left: 310px;
    top: 40px;
    width: 580px;
    height: 820px;
    overflow: hidden;
    box-shadow: 0 6px 18px rgba(0,0,0,0.12);
  }
  .cover-visual {
    position: absolute;
    inset: 0;
    background:
      radial-gradient(ellipse 38% 60% at 72% 30%, rgba(58,82,201,0.85), transparent 70%),
      radial-gradient(ellipse 30% 70% at 40% 55%, rgba(29,47,147,0.75), transparent 70%),
      radial-gradient(ellipse 45% 35% at 20% 80%, rgba(230,232,238,0.9), transparent 70%),
      radial-gradient(ellipse 40% 40% at 60% 78%, rgba(150,156,172,0.7), transparent 70%),
      linear-gradient(135deg, var(--steel) 0%, var(--steel-dark) 35%, var(--ribbon-deep) 55%, var(--ribbon-bright) 75%, #16226a 100%);
  }
  .brand-label {
    position: absolute;
    left: 38%;
    top: 0;
    width: 40%;
    height: 108px;
    background: var(--label-bg);
    display: flex;
    align-items: center;
    justify-content: center;
    gap: 12px;
  }
  .brand-dot {
    width: 34px;
    height: 34px;
    border-radius: 50%;
    background: var(--brand-blue);
    flex: none;
  }
  .brand-text { display: flex; flex-direction: column; line-height: 1; }
  .brand-name {
    font-weight: 700;
    font-size: 40px;
    color: var(--navy);
    letter-spacing: 1px;
  }
  .brand-region {
    font-size: 9px;
    font-weight: 400;
    color: var(--mid-blue);
    letter-spacing: 2px;
    margin-top: 5px;
    text-align: right;
  }
  .brand-tagline {
    font-size: 9px;
    font-weight: 400;
    color: var(--navy);
    margin-top: 3px;
    text-align: right;
  }
  .cover-title {
    position: absolute;
    left: 475px;
    top: 570px;
    transform: rotate(-90deg);
    transform-origin: left top;
    color: var(--white);
    font-weight: 100;
    font-size: 62px;
    line-height: 0.82;
    text-align: right;
    white-space: nowrap;
  }
  .cover-title span { display: block; }
</style>
</head>
<body>
  <main class="cover">
    <div class="cover-visual" role="img" aria-label="Close-up of polished steel gears with flowing blue lubricant ribbons"></div>
    <header class="brand-label">
      <div class="brand-dot"></div>
      <div class="brand-text">
        <span class="brand-name">VOREN</span>
        <span class="brand-region">AUSTRALIA</span>
        <span class="brand-tagline">Lubricants made in Germany</span>
      </div>
    </header>
    <h1 class="cover-title"><span>product</span><span>range</span></h1>
  </main>
</body>
</html>
```